Simple, Professional and neat business card design for Vendralo Inc.

We're looking to re-vamp our business card design. We're a supplier of innovative feed ingredients for the North American animal agriculture industry. We are located in Lucknow, Ontario, Canada and our flagship product is a product that prevents milk fever in dairy cows when the calve, it is fed before calving and is very effective compared to other alternatives available on the market today.

Our company has Danish roots and we import all of our product from our Danish partner/manufacturer in Denmark. We like our design to embrace high professionalism while remaining neat and simple.

Target Market(s)

B2B, Feed Mills, Veterinary Clinics, Large integrators/producers,

Industry/Entity Type

Agribusiness

Contact Information for Business Card

We like the rounded corners because they make the card easy to sit in a wallet and not many use it so it makes the card stand out, just possibly something to take account for during the design.

As you can also see on the sliders below, looking for a that simple but proffesional scandinavian design.

Requirements
Nice to have
• Rounded corners
Should not have
• Too vibrant

```html
<!DOCTYPE html>
<html lang="en">
<head>
<meta charset="utf-8">
<title>Vendralo Inc. – Business Card</title>
<link href="https://fonts.googleapis.com/css2?family=Lato:wght@400;700;900&display=swap" rel="stylesheet">
<style>
  :root {
    --bg: #e6e8eb;
    --card: #ffffff;
    --brand: #0a4fa3;
    --brand-mid: #0a73c4;
    --brand-light: #1a8fd6;
    --brand-deep: #07438d;
    --ink: #2b2f36;
    --muted: #7a808a;
    --line: #c9d3df;
  }
  * { box-sizing: border-box; margin: 0; padding: 0; }
  html, body { width: 1200px; height: 900px; overflow: hidden; }
  body {
    background: var(--bg);
    font-family: "Lato", Arial, sans-serif;
    display: flex;
    flex-direction: column;
    align-items: center;
    justify-content: center;
    gap: 56px;
  }
  .card {
    position: relative;
    width: 600px;
    height: 343px;
    background: var(--card);
    border-radius: 26px;
    overflow: hidden;
    box-shadow: 0 10px 28px rgba(20, 30, 50, 0.18);
  }

  /* Front: brand side */
  .card-front .swoosh { position: absolute; inset: 0; width: 100%; height: 100%; }
  .card-front .website {
    position: absolute;
    left: 62px;
    top: 38px;
    color: #ffffff;
    font-size: 12px;
    letter-spacing: 0.3px;
    white-space: nowrap;
    transform-origin: left top;
    transform: rotate(32deg);
  }
  .card-front .website::before {
    content: "";
    position: absolute;
    left: -30px;
    top: 7px;
    width: 20px;
    height: 2px;
    background: #ffffff;
  }
  .brand {
    display: flex;
    align-items: center;
    gap: 12px;
    color: var(--brand);
    font-weight: 900;
    text-transform: uppercase;
    letter-spacing: 0.5px;
    white-space: nowrap;
  }
  .brand-dot {
    border-radius: 50%;
    background: var(--brand);
    flex: none;
  }
  .card-front .brand { position: absolute; left: 262px; top: 142px; font-size: 28px; }
  .card-front .brand-dot { width: 36px; height: 36px; }

  /* Back: contact side */
  .card-back .person { position: absolute; left: 40px; top: 36px; }
  .contact-row {
    display: flex;
    align-items: flex-start;
    gap: 14px;
    margin-bottom: 12px;
  }
  .icon-box {
    width: 26px;
    height: 26px;
    border: 1px solid var(--line);
    display: flex;
    align-items: center;
    justify-content: center;
    flex: none;
    background: #fff;
  }
  .icon-box svg { width: 14px; height: 14px; }
  .person-name {
    color: var(--brand);
    font-weight: 900;
    font-size: 25px;
    line-height: 1;
    text-transform: uppercase;
    white-space: nowrap;
  }
  .person-role { color: var(--muted); font-size: 13px; margin-top: 3px; }
  .contact-text { color: var(--ink); font-size: 14px; line-height: 1.3; padding-top: 2px; }
  .contact-text .accent { color: var(--brand); }
  .contact-list { margin-top: 18px; }
  .card-back .brand { position: absolute; right: 38px; bottom: 34px; font-size: 24px; gap: 10px; }
  .card-back .brand-dot { width: 28px; height: 28px; }
</style>
</head>
<body>

  <section class="card card-front" aria-label="Business card front">
    <svg class="swoosh" viewBox="0 0 600 343" preserveAspectRatio="none" aria-hidden="true">
      <path d="M0 0 H300 C215 90 185 220 215 343 H0 Z" fill="var(--brand-mid)"/>
      <path d="M0 0 H215 C155 90 140 220 165 343 H0 Z" fill="var(--brand-light)" opacity="0.6"/>
      <path d="M0 0 H140 C100 100 95 230 115 343 H0 Z" fill="var(--brand)"/>
      <path d="M0 0 H60 C42 120 45 250 58 343 H0 Z" fill="var(--brand-deep)"/>
      <path d="M255 0 C185 90 165 220 190 343" stroke="#ffffff" stroke-opacity="0.16" stroke-width="8" fill="none"/>
    </svg>
    <span class="website">www.vendralo-feeds.com</span>
    <div class="brand"><span class="brand-dot"></span>Vendralo Inc.</div>
  </section>

  <section class="card card-back" aria-label="Business card back">
    <div class="person">
      <div class="contact-row">
        <span class="icon-box">
          <svg viewBox="0 0 16 16"><circle cx="8" cy="5" r="3" fill="none" stroke="var(--brand)" stroke-width="1.4"/><path d="M2.5 15c0-3.2 2.5-5 5.5-5s5.5 1.8 5.5 5" fill="none" stroke="var(--brand)" stroke-width="1.4"/></svg>
        </span>
        <div>
          <div class="person-name">Kasper Brennholt</div>
          <div class="person-role">Manager</div>
        </div>
      </div>
      <div class="contact-list">
        <div class="contact-row">
          <span class="icon-box">
            <svg viewBox="0 0 16 16"><path d="M4 1.5 L6.5 4.5 5 6.5 C6 8.5 7.5 10 9.5 11 L11.5 9.5 14.5 12 13 14.5 C7 14 2 9 1.5 3 Z" fill="var(--brand)"/></svg>
          </span>
          <div class="contact-text">014.582.3390<br>014.582.3391</div>
        </div>
        <div class="contact-row">
          <span class="icon-box">
            <svg viewBox="0 0 16 16" fill="none" stroke="var(--brand)" stroke-width="1.2"><circle cx="8" cy="8" r="6.5"/><ellipse cx="8" cy="8" rx="3" ry="6.5"/><path d="M1.5 8h13M2.5 4.5h11M2.5 11.5h11"/></svg>
          </span>
          <div class="contact-text">info@vendralo-feeds.com<br><span class="accent">www.vendralo-feeds.com</span></div>
        </div>
        <div class="contact-row">
          <span class="icon-box">
            <svg viewBox="0 0 16 16"><path d="M8 1a5 5 0 0 0-5 5c0 4 5 9 5 9s5-5 5-9a5 5 0 0 0-5-5z" fill="var(--brand)"/><circle cx="8" cy="6" r="1.8" fill="#fff"/></svg>
          </span>
          <div class="contact-text">1457 Maple Ridge Road<br>Lucknow, ON N0G 2H0</div>
        </div>
      </div>
    </div>
    <div class="brand"><span class="brand-dot"></span>Vendralo Inc.</div>
  </section>

</body>
</html>
```